Tallowmere Capital Partners- Business Card

We need a professional business card that conveys confidence and trust. Strength. A modern and still yet, traditional financial planner/advisor format. I will upload a logo file or two, you do not have to use it, if it does not work for the design.

Target Market(s)

high net worth

Industry/Entity Type

Finance

Contact Information for Business Card

Address: 24836 Orchard Ave. Suite 400, Huntington Beach, CA 93518, website: tallowmerecap.example, ph # (555) 271-6094, email address: rpoulsen@tallowmerecap.example

```html
<!DOCTYPE html>
<html lang="en">
<head>
<meta charset="utf-8">
<title>Tallowmere Capital Partners – Business Card</title>
<link href="https://fonts.googleapis.com/css2?family=Arimo:wght@400;700&family=Playfair+Display:wght@400&display=swap" rel="stylesheet">
<style>
  :root {
    --navy: #0b2468;
    --gold: #c9a543;
    --white: #ffffff;
    --page: #ecebe8;
    --text-light: #f2f4fa;
  }
  * { box-sizing: border-box; margin: 0; padding: 0; }
  html, body { width: 1200px; height: 977px; overflow: hidden; background: var(--page); }
  .sheet { position: relative; width: 1200px; height: 977px; }
  .card {
    position: absolute; left: 270px; width: 660px; height: 378px;
    background: var(--navy); border-radius: 22px; overflow: hidden;
    box-shadow: 0 6px 18px rgba(0,0,0,0.18);
  }
  .card--back { top: 60px; }
  .card--front { top: 538px; }

  .brand-line {
    position: absolute; left: 0; right: 0; top: 50%; transform: translateY(-50%);
    display: flex; align-items: center; justify-content: center; gap: 18px;
  }
  .brand-square { width: 40px; height: 40px; border: 2px solid var(--gold); }
  .brand-name {
    font-family: "Playfair Display", serif; font-weight: 400; font-size: 30px;
    font-variant: small-caps; letter-spacing: 0.5px; color: var(--white);
  }

  .front-art { position: absolute; inset: 0; }

  .panel-brand {
    position: absolute; left: 470px; top: 95px; width: 170px;
    display: flex; flex-direction: column; align-items: center; gap: 12px;
  }
  .panel-brand .brand-square { width: 46px; height: 46px; }
  .panel-name {
    font-family: "Playfair Display", serif; font-weight: 400; font-size: 21px;
    line-height: 1.2; color: var(--gold); text-align: center;
  }

  .person { position: absolute; left: 46px; top: 82px; width: 360px; }
  .person-name {
    font-family: "Arimo", sans-serif; font-weight: 700; font-size: 32px;
    color: var(--white); letter-spacing: 0.5px; white-space: nowrap;
  }
  .person-title {
    font-family: "Arimo", sans-serif; font-weight: 400; font-size: 20px;
    color: var(--gold); margin-top: 2px;
  }
  .contacts { list-style: none; margin-top: 20px; }
  .contacts li {
    display: flex; align-items: flex-start; gap: 14px;
    font-family: "Arimo", sans-serif; font-size: 15px; line-height: 21px;
    color: var(--text-light); white-space: nowrap;
  }
  .contacts li + li { margin-top: 2px; }
  .contacts .address { margin-bottom: 10px; }
  .icon { width: 16px; height: 16px; flex: none; margin-top: 3px; fill: var(--gold); }
</style>
</head>
<body>
<main class="sheet">

  <section class="card card--back" aria-label="Card back">
    <div class="brand-line">
      <span class="brand-square"></span>
      <span class="brand-name">Tallowmere Capital Partners</span>
    </div>
  </section>

  <section class="card card--front" aria-label="Card front">
    <svg class="front-art" width="660" height="378" viewBox="0 0 660 378">
      <defs>
        <radialGradient id="ring-tone" cx="0.5" cy="0.5" r="0.5">
          <stop offset="0.7" stop-color="#c9a543" stop-opacity="0"/>
          <stop offset="0.85" stop-color="#c9a543" stop-opacity="0.45"/>
          <stop offset="1" stop-color="#c9a543" stop-opacity="0"/>
        </radialGradient>
      </defs>
      <circle cx="540" cy="170" r="175" fill="url(#ring-tone)" role="img" aria-label="Gold decorative rings around the emblem"/>
      <path d="M470 0 H660 V250 L585 310 Q560 328 535 312 L430 240 Q408 224 414 198 L440 80 Z" fill="#ffffff"/>
    </svg>

    <div class="panel-brand">
      <span class="brand-square"></span>
      <span class="panel-name">Tallowmere Capital Partners</span>
    </div>

    <div class="person">
      <h1 class="person-name">DANIEL HARTWELL</h1>
      <p class="person-title">Creative Director</p>
      <ul class="contacts">
        <li class="address">
          <svg class="icon" viewBox="0 0 16 16"><path d="M8 0a5.5 5.5 0 0 0-5.5 5.5C2.5 10 8 16 8 16s5.5-6 5.5-10.5A5.5 5.5 0 0 0 8 0zm0 8a2.5 2.5 0 1 1 0-5 2.5 2.5 0 0 1 0 5z"/></svg>
          <span>24836 Orchard Ave. Suite 400<br>Huntington Beach, CA 93518</span>
        </li>
        <li>
          <svg class="icon" viewBox="0 0 16 16"><path d="M3.6 1 6 3.4 4.6 5.6a9 9 0 0 0 5.8 5.8l2.2-1.4L15 12.4 13 15C6.5 14.5 1.5 9.5 1 3z"/></svg>
          <span>(555) 271-6094</span>
        </li>
        <li>
          <svg class="icon" viewBox="0 0 16 16"><path d="M4 0h8a1 1 0 0 1 1 1v14a1 1 0 0 1-1 1H4a1 1 0 0 1-1-1V1a1 1 0 0 1 1-1zm1 2v10h6V2zm3 11a1 1 0 1 0 0 2 1 1 0 0 0 0-2z"/></svg>
          <span>(555) 271-6094</span>
        </li>
        <li>
          <svg class="icon" viewBox="0 0 16 16"><path d="M4 0h8v4H4zM1 5h14v7h-3v4H4v-4H1zm5 6v3h4v-3z"/></svg>
          <span>(555) 271-6094</span>
        </li>
        <li>
          <svg class="icon" viewBox="0 0 16 16"><path d="M0 3h16v10H0zm1.5 1.5 6.5 5 6.5-5v-.2H1.5z"/></svg>
          <span>rpoulsen@tallowmerecap.example</span>
        </li>
        <li>
          <svg class="icon" viewBox="0 0 16 16"><path d="M8 0a8 8 0 1 0 0 16A8 8 0 0 0 8 0zm0 1.5a6.5 6.5 0 1 1 0 13 6.5 6.5 0 0 1 0-13zM1.5 7.3h13v1.4h-13zM7.3 1.5h1.4v13H7.3z"/></svg>
          <span>tallowmerecap.example</span>
        </li>
      </ul>
    </div>
  </section>

</main>
</body>
</html>
```